Timeshare sales and holiday rental business needs a brochure design

We need a brochure design for a holiday company based in Aberfoyle Scotland. We sell and rent out timeshare holidays worldwide. We are looking for a A4 sized leaflet which we can insert text in which explains our business. The leaflet would A4 but would be folded into a DL size. The design should incorporate exotic beach holidays but also holidays in the Scottish Highlands. The emphasis should be on quality holidays for a fraction of the price it would cost elsewhere.

Target Market(s)

Holiday Market

Industry/Entity Type

Business

```html
<!DOCTYPE html>
<html lang="en">
<head>
<meta charset="utf-8">
<title>Lochside Escapes – Trifold Brochure</title>
<link href="https://fonts.googleapis.com/css2?family=Open+Sans:wght@400;600;700&display=swap" rel="stylesheet">
<style>
  :root {
    --green: #1f8a3c;
    --green-dark: #0f6a2a;
    --green-light: #7cc04b;
    --navy: #1d3f7a;
    --ink: #3d3d3d;
    --paper: #ffffff;
    --backdrop: #e6e6e6;
    --sky: #4c86cf;
    --sea: #5fc3d6;
    --sand: #e9dcc0;
    --row: #eef5ea;
  }
  * { box-sizing: border-box; margin: 0; padding: 0; }
  html, body { width: 1200px; height: 1200px; overflow: hidden; }
  body {
    background: var(--backdrop);
    font-family: "Open Sans", sans-serif;
    color: var(--ink);
    position: relative;
  }
  .spread {
    position: absolute;
    left: 190px;
    width: 820px;
    height: 580px;
    background: var(--paper);
    display: grid;
    grid-template-columns: repeat(3, 1fr);
    box-shadow: 0 4px 14px rgba(0,0,0,.18);
    overflow: hidden;
  }
  .spread--outside { top: 10px; }
  .spread--inside { top: 610px; }
  .panel { position: relative; overflow: hidden; border-right: 1px solid #ececec; }
  .panel:last-child { border-right: none; }
  .swoosh { position: absolute; left: 0; bottom: 0; width: 100%; }

  /* body copy */
  .copy p { font-size: 7.2px; line-height: 1.55; margin-bottom: 7px; }
  .heading-green { color: var(--green); font-weight: 700; }

  /* outside – about panel */
  .about { padding: 26px 20px 0; }
  .about h2 { font-size: 9px; margin-bottom: 6px; text-transform: uppercase; }

  /* outside – middle panel */
  .beach-band {
    position: absolute; left: 0; top: 0; width: 100%; height: 300px;
    background: linear-gradient(180deg, #2f63b7 0%, #7fb0e6 45%, var(--sea) 72%, var(--sand) 100%);
  }
  .sunset-circle {
    position: absolute; top: 130px; width: 92px; height: 92px; border-radius: 50%;
    border: 5px solid #fff;
    background: radial-gradient(circle at 50% 40%, #ffe39a 0%, #e7a43c 45%, #8a5a1e 100%);
    box-shadow: 0 2px 6px rgba(0,0,0,.3);
  }
  .sunset-circle--a { left: 34px; }
  .sunset-circle--b { left: 146px; }
  .contact-box {
    position: absolute; left: 22px; top: 340px; width: 220px;
    border: 1px solid #cfd8cf; border-radius: 6px; background: #fff;
    padding: 10px 12px; font-size: 7.5px; line-height: 1.6;
  }
  .contact-box h3 { font-size: 8.5px; color: var(--navy); margin-bottom: 4px; text-transform: uppercase; }

  /* outside – cover */
  .brand {
    display: flex; align-items: center; gap: 8px;
    color: var(--navy); font-weight: 700; font-size: 17px; letter-spacing: 1px; text-transform: uppercase;
  }
  .brand-dot { width: 26px; height: 26px; border-radius: 50%; background: var(--navy); flex: none; }
  .cover .brand { position: absolute; left: 30px; top: 30px; }
  .cover-photo {
    position: absolute; left: 0; top: 90px; width: 100%; height: 360px;
    background: linear-gradient(180deg, #3f78c8 0%, #8fbde8 40%, #4cc1d2 62%, #d8e8e6 80%, #eadfc6 100%);
  }
  .cover-web {
    position: absolute; right: 20px; bottom: 22px;
    color: #fff; font-size: 10px; font-weight: 600; letter-spacing: .5px;
  }

  /* inside */
  .highland-strip {
    position: absolute; left: 0; top: 0; width: 820px; height: 64px;
    background: linear-gradient(180deg, #8fb3d6 0%, #c6d9e6 35%, #5f8a45 60%, #2f5a2a 100%);
  }
  .shore-strip {
    position: absolute; left: 0; bottom: 0; width: 820px; height: 46px;
    background: linear-gradient(180deg, #3d5a3a 0%, #6b6f5d 50%, #3b3f37 100%);
  }
  .green-rule {
    position: absolute; left: 0; bottom: 46px; width: 820px; height: 22px;
    background: linear-gradient(180deg, var(--green-light) 0%, var(--green) 45%, var(--green-dark) 100%);
  }
  .inside-copy { position: absolute; top: 76px; left: 18px; right: 18px; }
  .inside-copy h2 { font-size: 9px; margin-bottom: 8px; line-height: 1.35; }
  .inside-copy .brand { font-size: 15px; margin-bottom: 14px; }
  .inside-copy .brand-dot { width: 22px; height: 22px; }

  .rental-table { width: 100%; border-collapse: collapse; font-size: 6.4px; margin: 6px 0 12px; }
  .rental-table th { background: var(--green-dark); color: #fff; font-weight: 600; padding: 3px 3px; text-align: left; }
  .rental-table td { padding: 3px 3px; border-bottom: 1px solid #dfe8da; }
  .rental-table tr:nth-child(even) td { background: var(--row); }

  .enquire { font-size: 7.5px; margin-bottom: 4px; }
  .phone-big { font-size: 19px; font-weight: 700; color: var(--ink); margin-bottom: 8px; }
  .email-big { font-size: 13px; font-weight: 700; color: var(--ink); }

  .testimonial-name { font-size: 7.4px; font-weight: 700; color: var(--green); margin-bottom: 2px; }
</style>
</head>
<body>

<!-- OUTSIDE SPREAD -->
<section class="spread spread--outside">
  <article class="panel about copy">
    <h2 class="heading-green">About us</h2>
    <p>Lochside Escapes has been helping families enjoy quality holidays for over twenty years. We buy, sell and rent timeshare weeks at resorts across the world, from sunny beaches to quiet Highland glens.</p>
    <p>Our friendly team knows every resort we offer and will match you with the right week, the right apartment and the right price for your party.</p>
    <p>Because we deal directly with owners, our guests enjoy luxury accommodation for a fraction of the price charged elsewhere, with no hidden fees.</p>
    <p>Whether you are looking for a short break, a family fortnight or a permanent holiday home, we are happy to talk you through every option.</p>
    <p>Our office is open Monday to Saturday. Call in, phone or email and we will reply within one working day.</p>
    <svg class="swoosh" viewBox="0 0 273 110" height="110" preserveAspectRatio="none" aria-hidden="true">
      <path d="M0 40 C90 70 190 70 273 30 L273 110 L0 110 Z" fill="var(--green)"/>
      <path d="M0 40 C90 70 190 70 273 30" fill="none" stroke="var(--green-light)" stroke-width="3"/>
    </svg>
  </article>

  <article class="panel">
    <div class="beach-band" role="img" aria-label="Tropical beach with blue sky and turquoise sea"></div>
    <svg class="swoosh" viewBox="0 0 273 300" height="300" preserveAspectRatio="none" aria-hidden="true" style="bottom:auto;top:260px">
      <path d="M0 40 C90 0 190 0 273 30 L273 300 L0 300 Z" fill="#fff"/>
    </svg>
    <div class="sunset-circle sunset-circle--a" role="img" aria-label="Friends playing on the beach at sunset"></div>
    <div class="sunset-circle sunset-circle--b" role="img" aria-label="Couple in the sea at sunset"></div>
    <div class="contact-box">
      <h3>Contact us</h3>
      Lochside Escapes Ltd, Birchwood House,<br>
      Glen Road, Strathmore, Scotland<br><br>
      T 01632 960390<br>
      F 01632 960391<br>
      hello@lochsideescapes.com
    </div>
    <svg class="swoosh" viewBox="0 0 273 110" height="110" preserveAspectRatio="none" aria-hidden="true">
      <path d="M0 30 C90 70 190 70 273 40 L273 110 L0 110 Z" fill="var(--green)"/>
      <path d="M0 30 C90 70 190 70 273 40" fill="none" stroke="var(--green-light)" stroke-width="3"/>
    </svg>
  </article>

  <article class="panel cover">
    <div class="brand"><span class="brand-dot"></span>Lochside Escapes</div>
    <div class="cover-photo" role="img" aria-label="Woman in a sun hat and sarong standing on a tropical shore"></div>
    <svg class="swoosh" viewBox="0 0 273 170" height="170" preserveAspectRatio="none" aria-hidden="true">
      <path d="M0 40 C40 110 150 110 273 20 L273 170 L0 170 Z" fill="var(--green)"/>
      <path d="M0 40 C40 110 150 110 273 20" fill="none" stroke="#fff" stroke-width="6"/>
      <path d="M0 46 C40 116 150 116 273 26" fill="none" stroke="var(--green-light)" stroke-width="3"/>
    </svg>
    <div class="cover-web">www.lochsideescapes.com</div>
  </article>
</section>

<!-- INSIDE SPREAD -->
<section class="spread spread--inside">
  <div class="highland-strip" role="img" aria-label="Scottish Highland hills under a pale sky"></div>

  <article class="panel copy">
    <div class="inside-copy">
      <div class="brand"><span class="brand-dot"></span>Lochside Escapes</div>
      <h2 class="heading-green">Worldwide Timeshare Rental Availability</h2>
      <p>We have a number of top quality timeshare and private villas to choose from.</p>
      <p>Below is a list of timeshare accommodation available across the world, or alternatively you can visit our website.</p>
      <p>If the dates you are looking for are not displayed below, please contact us by phone or email as we may be in a position to help.</p>
      <table class="rental-table">
        <tr><th>Dates</th><th>Resort</th><th>Type</th><th>Beds</th></tr>
        <tr><td>Jun 04–11</td><td>Costa Blanca</td><td>Apartment</td><td>2</td></tr>
        <tr><td>Jun 18–25</td><td>Algarve</td><td>Villa</td><td>3</td></tr>
        <tr><td>Jul 02–09</td><td>Tenerife</td><td>Apartment</td><td>1</td></tr>
        <tr><td>Jul 16–23</td><td>Glen Arden</td><td>Lodge</td><td>2</td></tr>
        <tr><td>Aug 06–13</td><td>Lanzarote</td><td>Villa</td><td>2</td></tr>
      </table>
      <p class="enquire">To book or enquire about any of the weeks below or any other date, please telephone our rentals office on</p>
      <div class="phone-big">01632 960390</div>
      <p class="enquire">or email:</p>
      <div class="email-big">hello@lochsideescapes.com</div>
    </div>
  </article>

  <article class="panel copy">
    <div class="inside-copy">
      <h2 class="heading-green">Quality Timeshare Resales and Timeshare Rentals Worldwide</h2>
      <p>Timeshare means a lifetime of luxury holidays in resorts around the world.</p>
      <p>Once you become a timeshare owner your range of holidays is almost endless. You can use your week at your home resort, or exchange it for a stay at thousands of resorts worldwide.</p>
      <p>If you are looking for a timeshare to purchase, look no further than Glen Arden Highland Club in the heart of Perthshire.</p>
      <p><span class="heading-green">WHY</span> choose Glen Arden Highland Club? Our prices are the lowest yearly maintenance fees in the UK.</p>
      <p>New fees from 1 July:<br>Studio sleeping 4 – £280<br>1 bed sleeping 4 – £345<br>2 bed sleeping 6 – £434<br>3 bed sleeping 8 – £466</p>
      <p><span class="heading-green">BECAUSE</span> the club is a five star resort with excellent exchange links and is guaranteed for the UK.</p>
      <p><span class="heading-green">BECAUSE</span> the location is simply stunning. All lodges sit beside the loch with lovely views of the hills.</p>
      <p><span class="heading-green">BECAUSE</span> it receives great reviews, rated 4.8 out of 5 by guests.</p>
      <p><span class="heading-green">BECAUSE</span> it is cheap to purchase. Weeks start from £99 including school holidays.</p>
    </div>
  </article>

  <article class="panel copy">
    <div class="inside-copy">
      <h2 class="heading-green">TESTIMONIALS</h2>
      <p>Below are just a few kind words from our guests. We value every comment and use them to keep improving our service.</p>
      <div class="testimonial-name">Mr &amp; Mrs Harlow, Leeds</div>
      <p>We have recently purchased a week at one of your resorts and wanted to say thank you for all your help. The whole process was easy and your staff were friendly from start to finish.</p>
      <div class="testimonial-name">Mr and Mrs Dunbar, Scotland</div>
      <p>We would absolutely recommend you to anyone thinking of buying or selling a timeshare. Keep up the excellent work.</p>
      <p>Just wanted to drop you a quick email to say we had a fantastic week in Spain. The apartment was perfect.</p>
      <div class="testimonial-name">Mrs Calloway, Former Owner at Pine Ridge</div>
      <p>I had a very positive experience with Lochside Escapes. The sale was quick and stress free. I was impressed.</p>
      <div class="testimonial-name">Mr and Mrs Ashby, Durham</div>
      <p>We are delighted that you have been able to sell the weeks so quickly.</p>
    </div>
  </article>

  <div class="green-rule"></div>
  <div class="shore-strip" role="img" aria-label="Rocky Highland shoreline"></div>
</section>

</body>
</html>
```